Menu Design Project For Crumbly Oak Sub Shop

We need a new menu designed for our sub shop that really captures the essence of who we are as a company. At Crumbly Oak Sub Shop we make everything BIG, if it isn't big then you will not find it in our restaurant. We are well known for our Cheese Steaks & Our Italian Subs. My idea for a menu is a 8 1/2 x 11 size double sided. I would like it to just be a crazy design such colorful and different. You can check out our Chatterbox for more company info. Crumbly Oak Sub Shop LLC. I am very open to all kinds of ideas and concepts as I love to be different then my competitors. Our main company colors are Red & Black. Also our logo needs to be included with our slogan Tall, Messy, Truly Loaded. Thanks

P.S.- Feel free to change up the layout as much as you would like.

Our Company Information
Crumbly Oak Sub Shop
718 Pelling Lane STE B
Seaford, DE 19846

Hi Everyone, Sorry for the late addition to the menu design but I just posted another link with a CAUTION warning I would like to add to the menu in some way. Thanks and please don't hesitate with any questions..

We have been getting some great designs! Please remember to put the chatterbox logo somewhere on the menu as we try to drive customers there.. Thanks!

Shop

• Company Logo
All Menu Products and Prices
Chatterbox Logo to drive clients to CB

```html
<!DOCTYPE html>
<html lang="en">
<head>
<meta charset="utf-8">
<title>Crumbly Oak Sub Shop Menu</title>
<link rel="stylesheet" href="https://fonts.googleapis.com/css2?family=Permanent+Marker&family=Gloria+Hallelujah&family=Rokkitt:wght@400;600&family=Open+Sans:wght@400;600&display=block">
<style>
:root{
  --stage:#e8e3dc;
  --red:#d3232a;
  --red-deep:#8c1016;
  --red-dark:#4a0a0d;
  --ink:#231619;
  --ink-2:#34232a;
  --yellow:#f6e400;
  --price:#e3282e;
  --white:#ffffff;
  --line:#bfb4b6;
  --steel:#b9c9cf;
  --marker:"Permanent Marker","Gloria Hallelujah",cursive;
}
*{box-sizing:border-box;margin:0;padding:0}
html,body{width:1200px;height:960px;overflow:hidden}
body{background:var(--stage);position:relative;font-family:"Rokkitt",Georgia,serif;color:var(--white)}

/* ---------- front side ---------- */
.menu-front{position:absolute;left:50px;top:53px;width:525px;height:812px;overflow:hidden;
  background:radial-gradient(ellipse at 45% 40%,var(--red) 0%,var(--red-deep) 60%,var(--red-dark) 100%)}
.slogan{position:absolute;font-family:var(--marker);text-transform:uppercase;line-height:1;white-space:nowrap}
.slogan-tall{left:28px;top:42px;font-size:52px;transform:rotate(-6deg)}
.slogan-messy{left:30px;top:96px;font-size:56px;color:var(--yellow);transform:rotate(-7deg)}
.slogan-loaded{left:36px;top:160px;font-size:34px;transform:rotate(-9deg)}

.brand-banner{position:absolute;left:14px;top:190px;width:526px;height:222px;background:var(--red);
  transform:rotate(-8deg);border-bottom:4px dotted var(--yellow);border-left:4px dotted var(--yellow);
  box-shadow:0 6px 16px rgba(0,0,0,.45)}
.cutlery{position:absolute;background:var(--steel);border-radius:12px}
.cutlery-fork{left:56px;top:74px;width:18px;height:112px}
.cutlery-knife{left:442px;top:38px;width:20px;height:140px}
.cutlery-spoon{left:474px;top:30px;width:24px;height:150px}
.brand-name{position:absolute;left:100px;top:66px;width:320px;display:flex;align-items:center;justify-content:center;gap:12px;
  font-family:var(--marker);font-size:38px;color:var(--white);white-space:nowrap}
.brand-name .mark{width:28px;height:28px;border-radius:50%;background:var(--white);flex:none}
.follow{position:absolute;left:200px;top:172px;display:flex;align-items:center;gap:6px;font-family:"Open Sans",Arial,sans-serif;font-size:15px;white-space:nowrap}
.follow .mark{width:18px;height:18px;background:#3b64b5;border-radius:3px}

.contact{position:absolute;left:104px;top:446px;transform:rotate(-7deg);transform-origin:left top;white-space:nowrap}
.contact .phone{font-family:"Open Sans",Arial,sans-serif;font-size:28px;font-weight:600}
.contact .address{font-family:"Open Sans",Arial,sans-serif;font-size:16px;margin-top:10px;line-height:1.3}
.contact .hours{font-family:"Open Sans",Arial,sans-serif;font-size:16px;color:var(--yellow)}

.food-photo{position:absolute;border:3px dotted var(--yellow);box-shadow:0 4px 10px rgba(0,0,0,.5)}
.photo-bacon{left:10px;top:695px;width:160px;height:118px;background:linear-gradient(135deg,#7a3b24,#c3683f 55%,#3d5a2a);transform:rotate(-2deg)}
.photo-sub{left:164px;top:620px;width:222px;height:192px;background:linear-gradient(160deg,#d79a55,#f1e6d2 45%,#e8d2b8 70%,#cf7433)}
.photo-salad{left:404px;top:672px;width:150px;height:140px;background:linear-gradient(135deg,#6f9a3a,#e9d46a 45%,#c98080 75%,#4e6f2a)}

/* ---------- back side ---------- */
.menu-back{position:absolute;left:613px;top:53px;width:527px;height:812px;background:linear-gradient(180deg,var(--ink-2),var(--ink))}
.outline{position:absolute;left:0;top:0;pointer-events:none}
.box{position:absolute;border:1.5px dashed var(--line);border-radius:12px;padding:6px 10px 0 12px}
.box h2,.condiments h2{font-family:var(--marker);font-weight:400;font-size:18px;color:var(--yellow);letter-spacing:.5px;line-height:1.25;margin-bottom:2px;text-transform:uppercase}
.item{display:flex;justify-content:space-between;font-size:14px;line-height:17.3px}
.item .price{color:var(--price)}
.label{color:var(--yellow);font-size:14px;line-height:17.3px}
.text{font-size:14px;line-height:17.3px}

.box-starters{left:5px;top:12px;width:287px;height:212px}
.box-sandwiches{left:302px;top:12px;width:218px;height:186px}
.caution{position:absolute;left:312px;top:206px;width:198px;height:88px;background:linear-gradient(180deg,#8e9090,#5f6263);padding:4px 8px;text-align:center}
.caution .title{font-family:var(--marker);font-size:32px;color:var(--yellow);line-height:1.1;letter-spacing:2px}
.caution .note{font-family:"Open Sans",Arial,sans-serif;font-size:7.4px;font-weight:600;color:var(--yellow);line-height:1.25;text-transform:uppercase}
.box-salads{left:5px;top:230px;width:287px;height:202px}
.box-salads .gap{height:17px}
.box-subs{left:302px;top:324px;width:218px;height:208px}
.subs-brand{position:absolute;left:366px;top:494px;display:flex;align-items:center;gap:6px;font-family:var(--marker);font-size:20px;color:var(--white);white-space:nowrap}
.subs-brand .mark{width:14px;height:14px;border-radius:50%;background:var(--white)}
.condiments{position:absolute;left:17px;top:445px;width:500px}
.condiments .item{width:265px}
.condiments .spacer{height:17px}
.box-specials{left:5px;top:647px;width:287px;height:140px}
.box-specials .item,.box-specials .label{font-size:15px;line-height:16px}
.box-specials .label{margin-top:6px}
.box-drinks{left:302px;top:647px;width:218px;height:140px}
.box-drinks .item{font-size:13.5px}
.box-drinks .text{font-size:13.5px;line-height:17px}
.footer{position:absolute;left:0;right:0;top:792px;text-align:center;font-family:"Open Sans",Arial,sans-serif;font-size:10.5px;font-weight:600}
.footer .price{color:var(--price)}
</style>
</head>
<body>

<section class="menu-front">
  <div class="slogan slogan-tall">Tall</div>
  <div class="slogan slogan-messy">Messy</div>
  <div class="slogan slogan-loaded">Truly Loaded</div>

  <div class="brand-banner">
    <div class="cutlery cutlery-fork" role="img" aria-label="Fork illustration"></div>
    <div class="cutlery cutlery-knife" role="img" aria-label="Knife illustration"></div>
    <div class="cutlery cutlery-spoon" role="img" aria-label="Spoon illustration"></div>
    <div class="brand-name"><span class="mark"></span>Crumbly Oak</div>
    <div class="follow">Follow Us On <span class="mark"></span> Chatterbox</div>
  </div>

  <div class="contact">
    <div class="phone">Phone : (302)-555-0148</div>
    <div class="address">Crumbly Oak Sub Shop,<br>718 Pelling Lane STE B, Millbrook ND, 19846.</div>
    <div class="hours">Hours : Monday- Saturday 11:00am- 7:00pm</div>
  </div>

  <div class="food-photo photo-bacon" role="img" aria-label="Photo of a bacon sandwich close-up"></div>
  <div class="food-photo photo-sub" role="img" aria-label="Photo of a loaded sub roll with fries"></div>
  <div class="food-photo photo-salad" role="img" aria-label="Photo of a chef salad with ham and cheese"></div>
</section>

<section class="menu-back">
  <svg class="outline" width="527" height="812" viewBox="0 0 527 812" aria-hidden="true">
    <path d="M17 439 H284 Q292 439 292 447 V541 H509 Q517 541 517 549 V629 Q517 637 509 637 H13 Q5 637 5 629 V447 Q5 439 13 439 Z"
      fill="none" stroke="#bfb4b6" stroke-width="1.5" stroke-dasharray="4 3"/>
  </svg>

  <div class="box box-starters">
    <h2>Starters</h2>
    <div class="item"><span>Broccoli Bites</span><span class="price">$ 4.29</span></div>
    <div class="item"><span>Small Fries</span><span class="price">$ 1.50</span></div>
    <div class="item"><span>Large Fries</span><span class="price">$ 2.95</span></div>
    <div class="item"><span>Fried Mushrooms</span><span class="price">$ 4.29</span></div>
    <div class="item"><span>Onion Rings</span><span class="price">$ 3.25</span></div>
    <div class="item"><span>Mozzarella Sticks (4)</span><span class="price">$ 4.00</span></div>
    <div class="item"><span>Chicken Tenders W/ Fries 3pc</span><span class="price">$ 4.00</span></div>
    <div class="item"><span>Chicken Tenders W/ Fries 5pc</span><span class="price">$ 7.00</span></div>
    <div class="item"><span>Wing Dings W/ Fries (6)</span><span class="price">$ 6.99</span></div>
    <div class="item"><span>Hushpuppies</span><span class="price">$ 4.99</span></div>
  </div>

  <div class="box box-sandwiches">
    <h2>Sandwiches</h2>
    <div class="item"><span>Grilled Hum &amp; Ch.</span><span class="price">$ 5.50</span></div>
    <div class="item"><span>BLT</span><span class="price">$ 4.99</span></div>
    <div class="item"><span>Burger</span><span class="price">$ 5.00</span></div>
    <div class="item"><span>Hot Dog</span><span class="price">$ 1.50</span></div>
    <div class="item"><span>Turkey</span><span class="price">$ 4.99</span></div>
    <div class="item"><span>Grilled Cheese</span><span class="price">$ 4.50</span></div>
    <div class="item"><span>Tuna or Chicken Salad</span><span class="price">$ 5.00</span></div>
    <div class="item"><span>Roast Beef</span><span class="price">$ 5.00</span></div>
  </div>

  <div class="caution">
    <div class="title">CAUTION</div>
    <div class="note">Purchase of a Crumbly Oak submarine sandwich may lead to confusion upon handling, please take care when attempting to eat our subs !!!!!!!!</div>
  </div>

  <div class="box box-salads">
    <h2>Salads</h2>
    <div class="item"><span class="label">Chef Salad</span><span class="price">$ 8.00</span></div>
    <div class="text">Mozzarella &amp; Sharp Cheese, Hum Turkey, Pepperoni, Tomato, Lettuce, Cucumbers, Onion, Croutons</div>
    <div class="gap"></div>
    <div class="item"><span class="label">Garden Salad</span><span class="price">$ 6.00</span></div>
    <div class="text">Onions, Green Peppers, Tomato, Carrots, Cucumbers, Sweet Pickles, Cheddar Cheese, Lettuce, Croutons</div>
  </div>

  <div class="box box-subs">
    <h2>Subs</h2>
    <div class="text">Hum, Turkey, Roast Beef Italian Or American Cold Cut CO Sub, Steak, Cheeseburger, Cheesesteak, Burger, CO Sub, Chicken Cheese Steak, Veggie, Chicken Salad, Cheese, Tuna Salad</div>
  </div>
  <div class="subs-brand"><span class="mark"></span>Crumbly Oak</div>

  <div class="condiments">
    <h2>Condiments</h2>
    <div class="item"><span>Extra Cheese/small Sub</span><span class="price">$ 0.50</span></div>
    <div class="item"><span>Extra Cheese/med-lge Sub</span><span class="price">$ 1.00</span></div>
    <div class="item"><span>Mushrooms</span><span class="price">$ 0.50</span></div>
    <div class="spacer"></div>
    <div class="item"><span>Extra Dressing</span><span class="price">$ 0.50</span></div>
    <div class="text">Pack Yellow American Cheese, Provolone, Swiss, Fried Raw Onions, Mayo, Green Peppers, Salt, Pepper, Relish, Regano, Lettuce, Tomato, Sweet Peppers, Sweet Pickles, Dil Pickles, Ketchup, Mustard, Oil, Vinegar, Bay Dust, Jalapenos, Banana Peppers, Hot Peppers, Black Olives</div>
  </div>

  <div class="box box-specials">
    <h2>Daily Specials</h2>
    <div class="label">Wednesday</div>
    <div class="item"><span>Turkey On Kaiser w/ fries</span><span class="price">$ 6.00</span></div>
    <div class="label" style="margin-top:18px">Thursday</div>
    <div class="item"><span>Small CheeseSteak w/fries &amp;<br>20 oz soda</span><span class="price" style="align-self:flex-end">$ 8.75</span></div>
  </div>

  <div class="box box-drinks">
    <h2>Cold Drinks</h2>
    <div class="item"><span>Sodas</span><span class="price">$ 1.50</span></div>
    <div class="item"><span>Thunder &amp; Calm Tea</span><span class="price">$ 2.00</span></div>
    <div class="text">CO- Cheese Steak w/y/a Cheese, Mayo, F.O., Hots, Lett, Tom, Swat Pic CO- Ham, Turkey&amp; Roast Beat Sab.</div>
  </div>

  <div class="footer">Small: $ <span class="price">6.75</span>, Medium: $ <span class="price">9.75</span>, Large: $ <span class="price">12.75</span> *Prices subject to change Without notice*</div>
</section>

</body>
</html>
```